Flyer für Tiertherapeutin
Eine sehr motivierte und kreative Designerin. Schon der erste Vorschlag war ganz nach meinen Vorstellungen.
Zielgruppe
Ich bin Tiertherapeutin für TCVM und Ernährungsberaterin für Hunde und Katzen. Mittels Akupunktur, Lasertherapie, Mykotherapie und Ernährungsberatung kommt es zu einer Linderung vorhandener Schmerzen, eine verbesserte Regulation der Organe und einer Steigerung das Wohlbefindens sowie Lebensqualität.
Zielgruppe sind überwiegend weibliche Hunde- und Katzenbesitzer mit erkrankten Tieren.
Aufgabenstellung
Flyer sollte klappbar sein. Logo und mein Name und Kontaktdaten sollten enthalten sein.

```html
<!DOCTYPE html>
<html lang="de">
<head>
<meta charset="utf-8">
<title>Pfotenruhe – Flyer</title>
<link rel="stylesheet" href="https://fonts.googleapis.com/css2?family=Poppins:wght@400;500;600;700&family=Roboto+Slab:wght@700&family=Permanent+Marker&display=swap">
<style>
:root{
  --bg:#a4a4a4;
  --white:#ffffff;
  --tan:#d39b62;
  --tan-light:#e7bf92;
  --olive:#5d5230;
  --olive-dark:#463d22;
  --ink:#1c1a16;
  --text:#3b362c;
}
*{box-sizing:border-box;margin:0;padding:0}
html,body{width:750px;height:1200px;overflow:hidden;background:var(--bg)}
.canvas{position:relative;width:750px;height:1200px;background:var(--bg)}
.panel{position:absolute;width:254px;height:540px;background:var(--white);overflow:hidden;font-family:'Poppins',sans-serif;color:var(--text)}
.panel--cover{left:112px;top:54px}
.panel--about{left:383px;top:54px}
.panel--service{left:112px;top:606px}
.panel--tcm{left:383px;top:606px}
.panel__bands{position:absolute;left:0;top:0;width:254px;height:540px}

.brand{position:absolute;left:0;top:14px;width:254px;text-align:center}
.brand__dot{display:block;width:46px;height:46px;margin:0 auto 8px;border-radius:50%;background:var(--tan)}
.brand__name{display:block;font-family:'Poppins',sans-serif;font-weight:700;font-size:25px;line-height:30px;color:var(--ink)}
.brand__owner{position:absolute;left:0;top:121px;width:254px;text-align:center;font-family:'Roboto Slab',serif;font-weight:700;font-size:8.5px;letter-spacing:2.4px;color:var(--ink)}

.contact{position:absolute;left:24px;top:494px;width:220px;display:grid;grid-template-columns:98px 122px;row-gap:5px;font-size:7px;font-weight:600;line-height:8px;color:var(--white)}
.contact__item{display:flex;align-items:flex-start;gap:3px}
.contact__icon{flex:none;width:8px;height:8px}

.photo{position:absolute;border-radius:50%}
.photo--portrait{left:17px;top:152px;width:108px;height:108px;border:4px solid var(--white);background:radial-gradient(circle at 50% 45%,#d8c2a8 0,#9a8d80 55%,#3f4556 100%)}
.photo--food{left:117px;top:333px;width:122px;height:122px;border:4px solid var(--white);background:radial-gradient(circle at 55% 45%,#d98a45 0,#a8424a 45%,#5e2a2c 100%)}
.photo--needle{left:15px;top:345px;width:108px;height:108px;background:radial-gradient(circle at 50% 50%,#c9aa86 0,#a68a6b 60%,#8a7766 100%)}
.photo--nutrition{left:114px;top:339px;width:120px;height:120px;border:4px solid var(--white);background:radial-gradient(circle at 50% 45%,#c9763a 0,#7a3a2c 50%,#222 100%)}

.cover-claim{position:absolute;left:10px;top:374px;width:234px;text-align:center}
.cover-claim__services{font-weight:700;font-size:13.5px;line-height:17px;color:var(--tan)}
.cover-claim__region{font-weight:500;font-size:14.5px;line-height:17px;color:var(--olive);margin-top:4px}

.hand-title{font-family:'Permanent Marker',cursive;color:var(--white)}
.about-name{position:absolute;left:126px;top:152px;width:120px;text-align:center;font-size:23px;line-height:24px;transform:rotate(-2deg)}
.about-text{position:absolute;left:18px;top:278px;width:218px;text-align:center;font-size:6.4px;line-height:8.2px}
.about-text p+p{margin-top:8px}
.about-slogan{position:absolute;left:0;top:430px;width:254px;text-align:center;font-family:'Permanent Marker',cursive;font-size:12.5px;color:var(--tan)}

.service-head{position:absolute;left:31px;top:152px;width:193px;height:19px;border-radius:10px;background:var(--olive);color:var(--white);text-align:center;font-weight:700;font-size:11px;line-height:19px}
.service-list{position:absolute;left:31px;top:180px;width:193px;list-style:none}
.service-list li{display:flex;gap:6px;padding:4px 0 5px;border-bottom:0.7px solid var(--tan-light);font-weight:600;font-size:8.6px;line-height:11px;color:var(--white)}
.service-list li:nth-child(n+6){border-bottom-color:transparent;width:86px}
.service-list li:nth-child(n+6) span{white-space:nowrap}
.service-list svg{flex:none;width:7px;height:7px;margin-top:2px}

.tcm-title{position:absolute;left:0;top:145px;width:254px;text-align:center;font-size:25px;line-height:28px;transform:rotate(-1.5deg)}
.tcm-text{position:absolute;left:20px;top:233px;width:214px;text-align:center;font-size:6.4px;line-height:8.2px}
.tcm-text p+p{margin-top:7px}
</style>
</head>
<body>
<div class="canvas">

  <!-- Cover panel -->
  <section class="panel panel--cover">
    <svg class="panel__bands" viewBox="0 0 254 540" aria-hidden="true">
      <path d="M0 300 Q140 325 254 258 L254 338 Q130 362 0 364 Z" fill="var(--tan)"/>
      <path d="M0 334 Q150 344 254 268" fill="none" stroke="var(--olive-dark)" stroke-width="9"/>
      <path d="M0 340 Q150 350 254 276" fill="none" stroke="var(--tan-light)" stroke-width="2"/>
      <path d="M120 366 Q200 358 254 334 L254 344 Q200 364 120 366 Z" fill="#e6e6e6"/>
      <path d="M0 450 Q130 470 254 442" fill="none" stroke="var(--tan)" stroke-width="10"/>
      <path d="M0 464 Q130 484 254 456 L254 540 L0 540 Z" fill="var(--olive)"/>
    </svg>
    <svg class="panel__bands" viewBox="0 0 254 540" role="img" aria-label="Foto: Katze und Hund liegen nebeneinander in der Sonne">
      <defs><linearGradient id="coverPhoto" x1="0" y1="0" x2="0" y2="1">
        <stop offset="0" stop-color="#b8c9d8"/><stop offset="0.35" stop-color="#8a7a4c"/>
        <stop offset="0.6" stop-color="#c98a45"/><stop offset="1" stop-color="#b5a58c"/></linearGradient></defs>
      <path d="M0 112 Q127 172 254 112 L254 262 Q150 335 0 330 Z" fill="url(#coverPhoto)"/>
    </svg>
    <div class="brand"><span class="brand__dot"></span><span class="brand__name">Pfotenruhe</span></div>
    <div class="brand__owner">LENA HARTWIG</div>
    <div class="cover-claim">
      <div class="cover-claim__services">Tierernährungsberatung •<br>TCVM • Akupunktur</div>
      <div class="cover-claim__region">in Karlsruhe und<br>Umgebung</div>
    </div>
    <div class="contact">
      <span class="contact__item"><svg class="contact__icon" viewBox="0 0 10 10"><circle cx="5" cy="5" r="5" fill="#fff"/><path d="M3 2.5l1 1-.5.8a4 4 0 0 0 2.2 2.2l.8-.5 1 1-.7.9C4.6 7.8 2.2 5.4 2.1 3.2z" fill="var(--olive)"/></svg>0151 - 0000 4821</span>
      <span class="contact__item"><svg class="contact__icon" viewBox="0 0 10 10"><circle cx="5" cy="5" r="5" fill="#fff"/><rect x="2.5" y="3.3" width="5" height="3.4" fill="none" stroke="var(--olive)" stroke-width=".8"/></svg>info@pfotenruhe-beispiel.de</span>
      <span class="contact__item"><svg class="contact__icon" viewBox="0 0 10 10"><circle cx="5" cy="5" r="5" fill="#fff"/><circle cx="5" cy="5" r="2.8" fill="none" stroke="var(--olive)" stroke-width=".7"/><path d="M2.2 5h5.6" stroke="var(--olive)" stroke-width=".7"/></svg>pfotenruhe-beispiel.de</span>
      <span class="contact__item"><svg class="contact__icon" viewBox="0 0 10 10"><path d="M5 0a3.6 3.6 0 0 1 3.6 3.6C8.6 6.4 5 10 5 10S1.4 6.4 1.4 3.6A3.6 3.6 0 0 1 5 0z" fill="#fff"/><circle cx="5" cy="3.6" r="1.3" fill="var(--olive)"/></svg>Birkenstraße 12 · 76131<br>Karlsruhe</span>
    </div>
  </section>

  <!-- About panel -->
  <section class="panel panel--about">
    <svg class="panel__bands" viewBox="0 0 254 540" aria-hidden="true">
      <path d="M0 112 Q127 172 254 112 L254 198 Q150 250 0 270 Z" fill="var(--tan)"/>
      <path d="M0 276 Q150 262 254 204" fill="none" stroke="var(--olive-dark)" stroke-width="7"/>
      <path d="M0 450 Q130 470 254 442" fill="none" stroke="var(--tan)" stroke-width="10"/>
      <path d="M0 464 Q130 484 254 456 L254 540 L0 540 Z" fill="var(--olive)"/>
    </svg>
    <div class="brand"><span class="brand__dot"></span><span class="brand__name">Pfotenruhe</span></div>
    <div class="brand__owner">LENA HARTWIG</div>
    <div class="photo photo--portrait" role="img" aria-label="Porträtfoto der Therapeutin mit einer weißen Katze"></div>
    <div class="about-name hand-title">Lena<br>Hartwig</div>
    <div class="about-text">
      <p>Mein Name ist Lena Hartwig.<br>Ich bin Tierernährungsberaterin für Hunde und Katzen, Akupunkteurin (TCVM) für Hunde, Katzen und Pferde und Katzenverhaltenstrainerin und somit in der optimalen Lage, die Erkrankung deines Tieres umfassend zu betrachten und zu behandeln.</p>
      <p>Mein Ziel ist es, den Körper deines Tieres in ein inneres Gleichgewicht zu bringen, die Selbstheilungskräfte zu aktivieren und dies führt zu einem schmerzfreien und gesunden Leben deines besten Fellfreundes.<br>Meine Therapiemethoden lindern nicht nur die Symptome, sondern lösen die Ursachen auf.</p>
      <p>Während der Behandlung ist es mir wichtig, dass sich dein Tier entspannt. Das kann es im gewohnten Umfeld am besten. Daher arbeite ich mobil im Raum Karlsruhe und Umgebung.</p>
    </div>
    <div class="about-slogan">Dein Tier in guten Händen!</div>
    <div class="contact">
      <span class="contact__item"><svg class="contact__icon" viewBox="0 0 10 10"><circle cx="5" cy="5" r="5" fill="#fff"/><path d="M3 2.5l1 1-.5.8a4 4 0 0 0 2.2 2.2l.8-.5 1 1-.7.9C4.6 7.8 2.2 5.4 2.1 3.2z" fill="var(--olive)"/></svg>0151 - 0000 4821</span>
      <span class="contact__item"><svg class="contact__icon" viewBox="0 0 10 10"><circle cx="5" cy="5" r="5" fill="#fff"/><rect x="2.5" y="3.3" width="5" height="3.4" fill="none" stroke="var(--olive)" stroke-width=".8"/></svg>info@pfotenruhe-beispiel.de</span>
      <span class="contact__item"><svg class="contact__icon" viewBox="0 0 10 10"><circle cx="5" cy="5" r="5" fill="#fff"/><circle cx="5" cy="5" r="2.8" fill="none" stroke="var(--olive)" stroke-width=".7"/><path d="M2.2 5h5.6" stroke="var(--olive)" stroke-width=".7"/></svg>pfotenruhe-beispiel.de</span>
      <span class="contact__item"><svg class="contact__icon" viewBox="0 0 10 10"><path d="M5 0a3.6 3.6 0 0 1 3.6 3.6C8.6 6.4 5 10 5 10S1.4 6.4 1.4 3.6A3.6 3.6 0 0 1 5 0z" fill="#fff"/><circle cx="5" cy="3.6" r="1.3" fill="var(--olive)"/></svg>Birkenstraße 12 · 76131<br>Karlsruhe</span>
    </div>
  </section>

  <!-- Service panel -->
  <section class="panel panel--service">
    <svg class="panel__bands" viewBox="0 0 254 540" aria-hidden="true">
      <path d="M0 112 Q127 172 254 112 L254 338 Q190 420 0 420 Z" fill="var(--tan)"/>
      <path d="M0 426 Q180 430 254 342" fill="none" stroke="var(--olive-dark)" stroke-width="7"/>
      <path d="M0 450 Q130 470 254 442" fill="none" stroke="var(--tan)" stroke-width="10"/>
      <path d="M0 464 Q130 484 254 456 L254 540 L0 540 Z" fill="var(--olive)"/>
    </svg>
    <div class="brand"><span class="brand__dot"></span><span class="brand__name">Pfotenruhe</span></div>
    <div class="brand__owner">LENA HARTWIG</div>
    <div class="service-head">UNSER SERVICE</div>
    <ul class="service-list">
      <li><svg viewBox="0 0 10 10"><circle cx="5" cy="5" r="5" fill="#fff"/><path d="M2.8 5.2l1.5 1.5 3-3.2" fill="none" stroke="var(--tan)" stroke-width="1.2"/></svg><span>Katzenverhaltenstraining</span></li>
      <li><svg viewBox="0 0 10 10"><circle cx="5" cy="5" r="5" fill="#fff"/><path d="M2.8 5.2l1.5 1.5 3-3.2" fill="none" stroke="var(--tan)" stroke-width="1.2"/></svg><span>Ernährungsberatung für Hunde<br>und Katzen</span></li>
      <li><svg viewBox="0 0 10 10"><circle cx="5" cy="5" r="5" fill="#fff"/><path d="M2.8 5.2l1.5 1.5 3-3.2" fill="none" stroke="var(--tan)" stroke-width="1.2"/></svg><span>Ganzheitliche Behandlung nach TCVM</span></li>
      <li><svg viewBox="0 0 10 10"><circle cx="5" cy="5" r="5" fill="#fff"/><path d="M2.8 5.2l1.5 1.5 3-3.2" fill="none" stroke="var(--tan)" stroke-width="1.2"/></svg><span>Chinesische Kräuterheilkunde</span></li>
      <li><svg viewBox="0 0 10 10"><circle cx="5" cy="5" r="5" fill="#fff"/><path d="M2.8 5.2l1.5 1.5 3-3.2" fill="none" stroke="var(--tan)" stroke-width="1.2"/></svg><span>Akupunktur</span></li>
      <li><svg viewBox="0 0 10 10"><circle cx="5" cy="5" r="5" fill="#fff"/><path d="M2.8 5.2l1.5 1.5 3-3.2" fill="none" stroke="var(--tan)" stroke-width="1.2"/></svg><span>Laserbehandlung</span></li>
      <li><svg viewBox="0 0 10 10"><circle cx="5" cy="5" r="5" fill="#fff"/><path d="M2.8 5.2l1.5 1.5 3-3.2" fill="none" stroke="var(--tan)" stroke-width="1.2"/></svg><span>Mykotherapie</span></li>
      <li><svg viewBox="0 0 10 10"><circle cx="5" cy="5" r="5" fill="#fff"/><path d="M2.8 5.2l1.5 1.5 3-3.2" fill="none" stroke="var(--tan)" stroke-width="1.2"/></svg><span>Darmaufbau</span></li>
    </ul>
    <div class="photo photo--food" role="img" aria-label="Foto: rohes Fleisch und Eigelb als Futter"></div>
    <div class="contact">
      <span class="contact__item"><svg class="contact__icon" viewBox="0 0 10 10"><circle cx="5" cy="5" r="5" fill="#fff"/><path d="M3 2.5l1 1-.5.8a4 4 0 0 0 2.2 2.2l.8-.5 1 1-.7.9C4.6 7.8 2.2 5.4 2.1 3.2z" fill="var(--olive)"/></svg>0151 - 0000 4821</span>
      <span class="contact__item"><svg class="contact__icon" viewBox="0 0 10 10"><circle cx="5" cy="5" r="5" fill="#fff"/><rect x="2.5" y="3.3" width="5" height="3.4" fill="none" stroke="var(--olive)" stroke-width=".8"/></svg>info@pfotenruhe-beispiel.de</span>
      <span class="contact__item"><svg class="contact__icon" viewBox="0 0 10 10"><circle cx="5" cy="5" r="5" fill="#fff"/><circle cx="5" cy="5" r="2.8" fill="none" stroke="var(--olive)" stroke-width=".7"/><path d="M2.2 5h5.6" stroke="var(--olive)" stroke-width=".7"/></svg>pfotenruhe-beispiel.de</span>
      <span class="contact__item"><svg class="contact__icon" viewBox="0 0 10 10"><path d="M5 0a3.6 3.6 0 0 1 3.6 3.6C8.6 6.4 5 10 5 10S1.4 6.4 1.4 3.6A3.6 3.6 0 0 1 5 0z" fill="#fff"/><circle cx="5" cy="3.6" r="1.3" fill="var(--olive)"/></svg>Birkenstraße 12 · 76131<br>Karlsruhe</span>
    </div>
  </section>

  <!-- TCM panel -->
  <section class="panel panel--tcm">
    <svg class="panel__bands" viewBox="0 0 254 540" aria-hidden="true">
      <path d="M0 112 Q127 172 254 112 L254 152 Q150 200 0 196 Z" fill="var(--tan)"/>
      <path d="M0 200 Q150 205 254 156" fill="none" stroke="var(--olive-dark)" stroke-width="7"/>
      <path d="M0 450 Q130 470 254 442" fill="none" stroke="var(--tan)" stroke-width="10"/>
      <path d="M0 464 Q130 484 254 456 L254 540 L0 540 Z" fill="var(--olive)"/>
    </svg>
    <div class="brand"><span class="brand__dot"></span><span class="brand__name">Pfotenruhe</span></div>
    <div class="brand__owner">LENA HARTWIG</div>
    <div class="tcm-title hand-title">Was ist TCM?</div>
    <div class="tcm-text">
      <p>Die traditionelle chinesische Medizin für Tiere (TCVM) ist ein ganzheitliches medizinisches System, das auf einer jahrtausendealten chinesischen Tradition basiert. Sie umfasst verschiedene Behandlungsmethoden wie Akupunktur, Moxibustion, Lasertherapie, Kräuterheilkunde, Ernährungstherapie und Tuina.</p>
      <p>Die TCVM (Traditionelle Chinesische Veterinärmedizin) betrachtet den tierischen Körper als ein komplexes System, das von der Lebensenergie „Qi“ durchströmt wird. Krankheiten entstehen, wenn das Qi aus dem Gleichgewicht gerät oder blockiert ist.</p>
    </div>
    <div class="photo photo--needle" role="img" aria-label="Foto: Akupunkturnadeln im Fell eines Hundes"></div>
    <div class="photo photo--nutrition" role="img" aria-label="Foto: Schüssel mit frischem Futter, Gemüse und Eiern"></div>
    <div class="contact">
      <span class="contact__item"><svg class="contact__icon" viewBox="0 0 10 10"><circle cx="5" cy="5" r="5" fill="#fff"/><path d="M3 2.5l1 1-.5.8a4 4 0 0 0 2.2 2.2l.8-.5 1 1-.7.9C4.6 7.8 2.2 5.4 2.1 3.2z" fill="var(--olive)"/></svg>0151 - 0000 4821</span>
      <span class="contact__item"><svg class="contact__icon" viewBox="0 0 10 10"><circle cx="5" cy="5" r="5" fill="#fff"/><rect x="2.5" y="3.3" width="5" height="3.4" fill="none" stroke="var(--olive)" stroke-width=".8"/></svg>info@pfotenruhe-beispiel.de</span>
      <span class="contact__item"><svg class="contact__icon" viewBox="0 0 10 10"><circle cx="5" cy="5" r="5" fill="#fff"/><circle cx="5" cy="5" r="2.8" fill="none" stroke="var(--olive)" stroke-width=".7"/><path d="M2.2 5h5.6" stroke="var(--olive)" stroke-width=".7"/></svg>pfotenruhe-beispiel.de</span>
      <span class="contact__item"><svg class="contact__icon" viewBox="0 0 10 10"><path d="M5 0a3.6 3.6 0 0 1 3.6 3.6C8.6 6.4 5 10 5 10S1.4 6.4 1.4 3.6A3.6 3.6 0 0 1 5 0z" fill="#fff"/><circle cx="5" cy="3.6" r="1.3" fill="var(--olive)"/></svg>Birkenstraße 12 · 76131<br>Karlsruhe</span>
    </div>
  </section>

</div>
</body>
</html>
```